Plakat-Design für eine Budgetplanung für ein Kinderbuch
Das vorgeschlagene Poster war von Anfang an unser Favorit. Es zeichnet sich aus, durch ein ansprechendes, klares und kindgerechtes Design. Wir haben die ausgesprochen zuverlässige Arbeit und Kommunikation sehr geschätzt und hoffen auf weitere Zusammenarbeit.
Zielgruppe
Wir sind ein Verlag und bringen nächsten Monat zwei Kinder-/Jugendbücher mit dem Thema Finanzbildung heraus. Das Alter der Zielgruppe ist zwischen 8 und 13 Jahren. Zu den Büchern gehört ein hochwertiges Posterset aus drei Postern. In diesem Auftrag soll zunächst das erste Poster designed werden. Hier geht es darum eine kleine 'Budgetplanung' zu erstellen. In weiteren Aufträgen sollen auch Illustrationen aufgewertet und Designs für Websites erstellt werden.
Aufgabenstellung
Wir werden einige Bilder bereitstellen, die verarbeitet werden dürfen (es müssen nicht alle verwendet werden!). Es wäre schön, wenn das Posterdesign so ausgelegt wird, dass die Bilder gut in das Gesamtdesign passen. Die Bildqualität des Posters soll auf DINA2 optimiert sein. Weiterhin stellen wir einen 'Beispiel-Geldplan' zur Verfügung, der alle Texte enthält, die das Poster beinhalten soll. Das Design dieses Beispiel-Geldplans soll unberücksichtigt bleiben. Das Gesamtdesign soll hochwertig und kreativ sein.

```html
<!DOCTYPE html>
<html lang="de">
<head>
<meta charset="utf-8">
<title>Wie ich mir meine Träume erfülle – Budgetplan</title>
<link href="https://fonts.googleapis.com/css2?family=Schoolbell&family=Inter:wght@300&display=swap" rel="stylesheet">
<style>
  :root{
    --blue:#3a78be;
    --purple-1:#b98bbf;--purple-2:#cda9d3;--purple-3:#dec5e2;--purple-4:#ebdff0;
    --green-1:#8fcfb1;--green-2:#b8dfcb;--green-3:#d9efe6;
    --yellow-1:#fddf62;--yellow-2:#fde99b;--yellow-3:#fdf0bd;--yellow-4:#fdf7df;
    --sky-1:#7096cf;--sky-2:#a4b7e1;--sky-3:#c2cfea;--sky-4:#dce2f3;
    --coin:#f9e42a;--ink:#1d1d1b;--white:#fff;
  }
  html,body{margin:0;padding:0;overflow:hidden;background:var(--white)}
  .canvas{position:relative;width:900px;height:1200px;overflow:hidden;background:var(--white)}
  .poster{position:absolute;left:56px;top:43px;width:788px;height:1112px;border:1px solid var(--blue);box-sizing:border-box;background:var(--white)}
  .header-band{position:absolute;left:56px;top:43px;width:788px;height:167px;background:var(--blue)}
  .footer-band{position:absolute;left:56px;top:1129px;width:788px;height:26px;background:var(--blue)}
  .title{position:absolute;left:98px;top:62px;margin:0;font-family:"Schoolbell",cursive;font-weight:400;
    color:var(--white);font-size:58px;line-height:64px;letter-spacing:1px;white-space:nowrap}
  .label{position:absolute;font-family:"Schoolbell",cursive;color:var(--ink);font-size:21px;line-height:24px;text-align:right;font-weight:700;letter-spacing:.5px;white-space:nowrap}
  .sublabel{position:absolute;font-family:"Inter",sans-serif;font-weight:300;color:var(--ink);font-size:18px;line-height:22px;text-align:right;white-space:nowrap}
  .bar{position:absolute;height:32px}
  .illustration{position:absolute;border-radius:20px}
  .coin{position:absolute;width:22px;height:22px;border-radius:50%;background:var(--coin);border:1.5px solid var(--ink);box-sizing:border-box}
</style>
</head>
<body>
<div class="canvas">
  <div class="poster"></div>
  <div class="header-band"></div>
  <div class="footer-band"></div>
  <h1 class="title">Wie ich mir meine<br>Träume erfülle</h1>

  <!-- Einnahmen -->
  <div class="label" style="right:488px;top:242px">Ich bekomme jeden Monat:</div>
  <div class="bar" style="left:428px;top:238px;width:168px;background:var(--purple-1)"></div>
  <div class="sublabel" style="right:488px;top:290px">Davon Taschengeld:</div>
  <div class="bar" style="left:428px;top:278px;width:168px;background:var(--purple-2)"></div>
  <div class="sublabel" style="right:488px;top:330px">Aus meinem Verdienst:</div>
  <div class="bar" style="left:428px;top:318px;width:168px;background:var(--purple-3)"></div>
  <div class="sublabel" style="right:488px;top:370px">Durch meine Investition:</div>
  <div class="bar" style="left:428px;top:356px;width:168px;background:var(--purple-4)"></div>

  <!-- Ausgaben -->
  <div class="label" style="right:492px;top:444px">Ich brauche jeden Monat<br>für Freizeit, Essen etc.:</div>
  <div class="bar" style="left:424px;top:441px;width:168px;background:var(--green-1)"></div>
  <div class="label" style="right:496px;top:542px">Ich möchte investieren:</div>
  <div class="bar" style="left:424px;top:538px;width:168px;background:var(--green-2)"></div>
  <div class="label" style="right:496px;top:596px">Ich möchte spenden:</div>
  <div class="bar" style="left:424px;top:592px;width:168px;background:var(--green-3)"></div>

  <!-- Sparen -->
  <div class="label" style="right:434px;top:688px">Ich möchte sparen:</div>
  <div class="bar" style="left:481px;top:685px;width:168px;background:var(--yellow-1)"></div>
  <div class="sublabel" style="right:434px;top:738px">Wunsch 1:</div>
  <div class="bar" style="left:481px;top:725px;width:168px;background:var(--yellow-2)"></div>
  <div class="sublabel" style="right:434px;top:778px">Wunsch 2:</div>
  <div class="bar" style="left:481px;top:765px;width:168px;background:var(--yellow-3)"></div>
  <div class="sublabel" style="right:434px;top:817px">Wunsch 3:</div>
  <div class="bar" style="left:481px;top:803px;width:168px;background:var(--yellow-4)"></div>
  <div class="label" style="right:434px;top:872px">Ich habe schon gespart:</div>
  <div class="bar" style="left:481px;top:869px;width:168px;background:var(--yellow-1)"></div>

  <!-- Ziele -->
  <div class="label" style="right:310px;top:946px">Meine Träume werden wahr in:</div>
  <div class="bar" style="left:608px;top:941px;width:169px;background:var(--sky-1)"></div>
  <div class="sublabel" style="right:310px;top:995px">Wunsch 1:</div>
  <div class="bar" style="left:608px;top:982px;width:169px;background:var(--sky-2)"></div>
  <div class="sublabel" style="right:310px;top:1035px">Wunsch 2:</div>
  <div class="bar" style="left:608px;top:1021px;width:169px;background:var(--sky-3)"></div>
  <div class="sublabel" style="right:310px;top:1074px">Wunsch 3:</div>
  <div class="bar" style="left:608px;top:1062px;width:169px;background:var(--sky-4)"></div>

  <!-- Illustrationen -->
  <div class="illustration" role="img" aria-label="Illustration: bunte Fantasiewesen auf einer Schaukel und einem Brett mit Goldmünzen" style="left:602px;top:95px;width:242px;height:380px;background:linear-gradient(160deg,#f4e79a,#e58bb3 60%,#d9b08c)"></div>
  <div class="illustration" role="img" aria-label="Illustration: blaues Fantasiewesen rechnet an einer Tafel, darüber Glühbirnen" style="left:109px;top:270px;width:88px;height:160px;background:linear-gradient(180deg,#f6e9a6,#9ecbea)"></div>
  <div class="illustration" role="img" aria-label="Illustration: oranges Fantasiewesen hält ein Euro-Zeichen" style="left:599px;top:482px;width:40px;height:116px;background:linear-gradient(180deg,#f5d2b8,#ee8a4a)"></div>
  <div class="illustration" role="img" aria-label="Illustration: drei Fantasiewesen tragen ein rosa Sparschwein" style="left:658px;top:525px;width:186px;height:276px;background:linear-gradient(180deg,#ee8fb1,#9fa6e0 60%,#f6df6a)"></div>
  <div class="illustration" role="img" aria-label="Illustration: Fantasiewesen mit Sparschwein und einem Wagen voller Goldmünzen" style="left:119px;top:722px;width:212px;height:132px;background:linear-gradient(120deg,#f5c7cf,#b6dca0 60%,#f6e27a)"></div>
  <div class="illustration" role="img" aria-label="Illustration: großes oranges Fantasiewesen blickt nach oben" style="left:76px;top:904px;width:130px;height:225px;background:linear-gradient(180deg,#f7efe6,#f29a2e)"></div>

  <!-- Münzen -->
  <div class="coin" style="left:575px;top:135px"></div>
  <div class="coin" style="left:565px;top:166px"></div>
  <div class="coin" style="left:596px;top:166px"></div>
  <div class="coin" style="left:749px;top:501px"></div>
  <div class="coin" style="left:749px;top:815px"></div>
  <div class="coin" style="left:400px;top:1003px"></div>
  <div class="coin" style="left:294px;top:1020px"></div>
  <div class="coin" style="left:225px;top:1081px"></div>
</div>
</body>
</html>
```